Luxury Business Card Design for High-End Window Treatments

Gilded Slatworks
Custom Plantation Shutters & Architectural Shading Systems

⸻

BACK

Daniel Ferrowitz
Owner

Custom Interior & Exterior Window Treatments

919-555-0187
gildedslatworks.example

I have included a picture that I’m hoping we can use on the back, but I’m also wondering if you can get rid of the ladder? Should we get rid of shutters , shades and blinds underneath Gilded Slatworks?

Target Market(s)

High-end residential homeowners, custom home builders, architects, interior designers, and luxury renovation clients seeking premium plantation shutters and motorized architectural shading systems.

Industry/Entity Type

Custom Window treatments

Contact Information for Business Card

Front Gilded Slatworks Custom Plantation Shutters Motorized Architectural Shading Systems BACK Daniel Ferrowitz Owner 919-555-0187 GildedSlatworks.example Custom Interior & Exterior Window Treatments By Appointment

Requirements
Nice to have
• Not 100% sure on nice to halves or the color but you can definitely check out my website to get a better understanding of what I’m trying to do

```html
<!DOCTYPE html>
<html lang="en">
<head>
<meta charset="utf-8">
<title>Gilded Slatworks – Business Card</title>
<link href="https://fonts.googleapis.com/css2?family=Sorts+Mill+Goudy&family=Libre+Baskerville:wght@700&family=Arimo:ital@0;1&display=swap" rel="stylesheet">
<style>
  :root {
    --backdrop: #e4e4e4;
    --card-top: #444444;
    --card-bottom: #2d2d2d;
    --gold: #c7ab5c;
    --ink-light: #f4f4f4;
    --divider: #8a8a8a;
  }
  html, body {
    margin: 0;
    width: 1200px;
    height: 1200px;
    overflow: hidden;
    background: var(--backdrop);
  }
  .canvas { position: relative; width: 1200px; height: 1200px; }
  .card {
    position: absolute;
    width: 687px;
    height: 392px;
    border-radius: 26px;
    background: linear-gradient(180deg, var(--card-top) 0%, var(--card-bottom) 100%);
    overflow: hidden;
  }
  .card--front { left: 267px; top: 159px; }
  .card--back  { left: 263px; top: 655px; }

  .wordmark {
    position: absolute;
    font-family: "Sorts Mill Goudy", serif;
    color: var(--gold);
    text-align: center;
    line-height: 1;
    white-space: nowrap;
  }
  .wordmark__line { display: block; }
  .wordmark__services { display: block; word-spacing: 0.5em; }

  .card--front .wordmark { left: 82px; top: 132px; width: 245px; font-size: 46px; }
  .card--front .wordmark__line + .wordmark__line { margin-top: 6px; }
  .card--front .wordmark__services { font-size: 17px; margin-top: 8px; }

  .card--back .wordmark { left: 0; width: 100%; top: 136px; font-size: 62px; }
  .card--back .wordmark__line + .wordmark__line { margin-top: 6px; }
  .card--back .wordmark__services { font-size: 23px; margin-top: 12px; }

  .divider {
    position: absolute;
    left: 338px; top: 104px;
    width: 1px; height: 150px;
    background: linear-gradient(180deg, transparent, var(--divider) 20%, var(--divider) 80%, transparent);
  }
  .person { position: absolute; left: 362px; top: 113px; }
  .person__name {
    font-family: "Libre Baskerville", serif;
    font-weight: 700;
    font-size: 21px;
    color: var(--gold);
    margin: 0;
    line-height: 1;
  }
  .person__role {
    font-family: "Arimo", sans-serif;
    font-size: 14px;
    color: var(--ink-light);
    margin: 6px 0 0;
  }
  .contact {
    position: absolute; left: 361px; top: 191px;
    margin: 0; padding: 0; list-style: none;
    font-family: "Arimo", sans-serif;
    font-size: 16px;
    color: var(--ink-light);
  }
  .contact__item { display: flex; align-items: center; height: 20.5px; }
  .contact__icon { width: 14px; height: 14px; margin-right: 12px; fill: var(--gold); }
  .tagline {
    position: absolute; left: 0; width: 100%; top: 339px;
    text-align: center; margin: 0;
    font-family: "Arimo", sans-serif; font-style: italic;
    font-size: 15.5px; color: var(--ink-light);
  }
  .tagline__amp { color: var(--gold); }
</style>
</head>
<body>
<div class="canvas">
  <section class="card card--front" aria-label="Business card front">
    <div class="wordmark">
      <span class="wordmark__line">Gilded</span>
      <span class="wordmark__line">Slatworks</span>
      <span class="wordmark__services">Shutters Shades Blinds</span>
    </div>
    <div class="divider"></div>
    <div class="person">
      <h1 class="person__name">Daniel Ferrowitz</h1>
      <p class="person__role">Owner</p>
    </div>
    <ul class="contact">
      <li class="contact__item">
        <svg class="contact__icon" viewBox="0 0 24 24" aria-hidden="true"><path d="M6.6 10.8a15.1 15.1 0 0 0 6.6 6.6l2.2-2.2c.3-.3.7-.4 1-.2 1.1.4 2.3.6 3.6.6.6 0 1 .4 1 1V20c0 .6-.4 1-1 1A17 17 0 0 1 3 4c0-.6.4-1 1-1h3.5c.6 0 1 .4 1 1 0 1.3.2 2.5.6 3.6.1.3 0 .7-.2 1z"/></svg>
        919-555-0187
      </li>
      <li class="contact__item">
        <svg class="contact__icon" viewBox="0 0 24 24" aria-hidden="true"><path d="M2 6h20v12H2z M2 6l10 7 10-7" fill="none" stroke="#c7ab5c" stroke-width="2"/></svg>
        info@gildedslatworks.example
      </li>
      <li class="contact__item">
        <svg class="contact__icon" viewBox="0 0 24 24" aria-hidden="true"><circle cx="12" cy="12" r="10"/><path d="M2 12h20M12 2c3 3 3 17 0 20M12 2c-3 3-3 17 0 20" fill="none" stroke="#2f2f2f" stroke-width="1.5"/></svg>
        www.gildedslatworks.example
      </li>
    </ul>
    <p class="tagline">Custom Interior <span class="tagline__amp">&amp;</span> Exterior Window Treatments</p>
  </section>

  <section class="card card--back" aria-label="Business card back">
    <div class="wordmark">
      <span class="wordmark__line">Gilded</span>
      <span class="wordmark__line">Slatworks</span>
      <span class="wordmark__services">Shutters Shades Blinds</span>
    </div>
  </section>
</div>
</body>
</html>
```